Tove & Lark Designs - Promotions flyer

I am a locally based Interior designer /stylist on Sydney's lower north shore. I would like to offer my services:
Full Professional Styling Services and Furniture Hire
Colour Consultation – Interior / exterior
Floor Coverings
Furniture selection and sourcing
Window Treatments
Wallpaper
Soft Furnishings
Upholstery
Renovations

I would like to offer a free consultation
Updates

Project Deadline Extended
Reason: I've been speaking with a designer and need her to make one more change. I have tried to message her twice, but have had no reply. Once she makes these changes I'm ready to sign off on the design. Thanks Harriet

Target Market(s)

30 - 60's middle to high income earners

Industry/Entity Type

Floor

Requirements
Must have
• one sided DL size
Use my logo
1 or 2 images of interior space or image of a lamp, cushion, lounge etc
The following contact details:
Mobile: 041 xxx xxxx
Website Address: www.tovelarkdesigns.example.au

```html
<!DOCTYPE html>
<html lang="en">
<head>
<meta charset="utf-8">
<title>Tove &amp; Lark Designs – Promotions Flyer</title>
<link rel="stylesheet" href="https://fonts.googleapis.com/css2?family=Questrial&family=Roboto+Condensed:wght@400;700&display=swap">
<style>
  :root {
    --orange: #ee6a2f;
    --grey-dark: #5d5e60;
    --grey-mid: #8a8b8d;
    --stone: #b9b3aa;
    --beige: #d9d2c5;
    --white: #ffffff;
    --ink: #231f20;
  }
  * { margin: 0; padding: 0; box-sizing: border-box; }
  html, body { width: 1200px; height: 2523px; overflow: hidden; background: var(--white); }
  .flyer { position: relative; width: 1200px; height: 2523px; overflow: hidden; background: var(--white); font-family: "Questrial", sans-serif; color: var(--ink); }

  .brand { position: absolute; top: 28px; left: 0; width: 1200px; text-align: center; color: var(--orange); font-family: "Questrial", sans-serif; line-height: 1; }
  .brand__name { font-size: 112px; letter-spacing: 1px; }
  .brand__sub { font-size: 96px; margin-top: 10px; }

  .backdrop { position: absolute; top: 290px; left: 0; width: 1200px; height: 750px; background: var(--beige); }

  .hero-photo { position: absolute; top: 300px; left: 170px; width: 940px; height: 610px; background: var(--white); padding: 12px; box-shadow: 0 10px 26px rgba(0,0,0,.35); }
  .hero-photo__fill { width: 100%; height: 100%; background: linear-gradient(180deg, #e9ecee 0%, #f7f7f5 45%, #d6d3cf 70%, #efefec 100%); }

  .tagline { position: absolute; top: 860px; left: 715px; width: 500px; height: 640px; background: var(--orange); border: 12px solid var(--white); box-shadow: 0 10px 24px rgba(0,0,0,.35); transform: rotate(-8deg); text-align: center; color: var(--white); font-family: "Questrial", sans-serif; line-height: 1; padding-top: 34px; }
  .tagline__line { font-size: 74px; }
  .tagline__accent { color: var(--stone); font-size: 88px; }
  .tagline__accent--big { font-size: 100px; }
  .tagline__strong { font-size: 112px; font-weight: 700; font-family: "Roboto Condensed", sans-serif; }

  .services { position: absolute; top: 1010px; left: 125px; width: 580px; }
  .services__title { font-family: "Roboto Condensed", sans-serif; font-weight: 700; font-size: 48px; line-height: 1.12; color: var(--ink); }
  .services__list { list-style: none; margin-top: 54px; font-family: "Roboto Condensed", sans-serif; font-size: 42px; line-height: 1.15; color: var(--ink); white-space: nowrap; }

  .offer-band { position: absolute; top: 0; left: 0; }
  .offer-band__free { font-family: "Roboto Condensed", sans-serif; font-weight: 700; font-size: 84px; fill: var(--white); }
  .offer-band__label { font-family: "Questrial", sans-serif; font-size: 96px; fill: var(--white); }

  .detail-photo { position: absolute; top: 1930px; left: 0; width: 1200px; height: 465px; background: linear-gradient(90deg, #f3f1ee 0%, #e4eee8 30%, #f6f4f2 60%, #f1d5e0 85%, #ecc9d6 100%); }

  .contact { position: absolute; top: 2395px; left: 0; width: 1200px; height: 128px; background: var(--grey-dark); color: var(--white); text-align: center; font-family: "Questrial", sans-serif; font-size: 50px; line-height: 1.15; padding-top: 8px; }
</style>
</head>
<body>
<main class="flyer">
  <header class="brand">
    <div class="brand__name">Tove &amp; Lark</div>
    <div class="brand__sub">Designs</div>
  </header>

  <div class="backdrop"></div>

  <figure class="hero-photo">
    <div class="hero-photo__fill" role="img" aria-label="Bright open-plan living room with white lounges and a double-height window"></div>
  </figure>

  <section class="services">
    <h2 class="services__title">Full Professional<br>Styling Services<br>and Furniture Hire</h2>
    <ul class="services__list">
      <li>Colour Consultation</li>
      <li>– Interior / exterior</li>
      <li>Floor Coverings</li>
      <li>Window Treatments</li>
      <li>Wallpaper</li>
      <li>Furniture selection and sourcing</li>
      <li>Soft Furnishings</li>
      <li>Upholstery</li>
      <li>Renovations</li>
    </ul>
  </section>

  <div class="tagline">
    <div class="tagline__line">We Take</div>
    <div class="tagline__accent">SPACE</div>
    <div class="tagline__line">and</div>
    <div class="tagline__line">Make it</div>
    <div class="tagline__accent tagline__accent--big">YOUR</div>
    <div class="tagline__strong">PLACE!</div>
  </div>

  <svg class="offer-band" width="1200" height="2523" viewBox="0 0 1200 2523">
    <polygon points="445,1705 1200,1545 1200,1775 480,1895" fill="var(--grey-dark)"/>
    <polygon points="480,1895 1200,1775 1200,1808 486,1925" fill="var(--orange)"/>
    <g transform="translate(525,1770) rotate(-12)">
      <text class="offer-band__free" x="0" y="0">FREE</text>
      <text class="offer-band__label" x="10" y="86">Consultation</text>
    </g>
  </svg>

  <div class="detail-photo" role="img" aria-label="Close-up of decor pieces: a green letter Z, a small figurine and a pink flower ornament"></div>

  <footer class="contact">
    <div>Mobile: 041 xxx xxxx</div>
    <div>www.tovelarkdesigns.example.au</div>
  </footer>
</main>
</body>
</html>
```